Brand Packaging Identity H
ZOLT WATCHES
Dear Designers,
Thanks everyone for there contribution and efforts, we shall finalize the project in a day.
Many thanks once again,
Regards,
PH
Thank you
have you decided yet?
LAST 2 days to go...
Goodluck,
The project has been extended for 4 days more, please understand our requirements and post your drafts.
Thanks,
#90 Please use original brand identity in your designs.
The project has been extended for 4 days, please submit your designs and we hope you'll meet the expectations.
Thank you all for your efforts, the contest will be over in next 10 hours. Please recharge your enthusiasm and strike your new ideas in new designs.
All the best,
Please be different in Watch Gift Box designing and Watch Tags designing, its not just an identical design on every item but its about creating new standards and new styles for a better usage. So, please be creative and innovative, all submitted drafts have almost similar stuff with a difference in design and art. Please add new and fresh ideas.
All goodluck, JUST ONE DAY TO GO.
Come'on Designers Buck up, its just 2 days more... send your designs and get over it.
#49: Please use the exact identity in your designs and instead of black gray could be a nicer combination.
Also try in another design combination near to the requirements.
#64: One star for the watch Pad and polybag, other identities could be much better please make it more appealing.
Rgds.,
#67: Zolt is a trendy digital watch, we appreciate your efforts, could be better.
the project has been extended for 3 days, please submit your designs soon.
Hello Ph,
Please check your private message at upper right corner.
#50: Zolt is a trendy digital watch.
Please be innovative in your work, there could be much better designs that draws better impact to the mind and leaves a lasting impression. Please submit those designs.
JUST A DAY TO GO...
Goodluck ALL,
#43: made it so simple, please be unique remember its a trendy digital watch, fresh ideas will be appreciated.
#44: You are a bit creative, but please use light colors in your designs, we value your efforts.
#45: We are looking for light color identity, your designs are good but would be much better if light background was used.
lets be active and make your creativity and concepts flow in designs.
Goodluck everyone,
rgds.,
The project has been extended for 3 days, please submit your fresh designs soon.

```html
<!DOCTYPE html>
<html lang="en">
<head>
<meta charset="utf-8">
<title>Zolt Watches – Packaging Identity</title>
<link href="https://fonts.googleapis.com/css2?family=Exo+2:wght@700;800&family=Roboto:wght@400;700&display=swap" rel="stylesheet">
<style>
:root{
  --bg:#eceded;
  --blue:#1d9ce2;
  --blue-deep:#0a78c6;
  --blue-light:#5cc0f2;
  --white:#ffffff;
  --silver:#c9cdd1;
  --silver-dark:#8d9399;
  --line:#b9c3cc;
  --ink:#123a5a;
}
*{margin:0;padding:0;box-sizing:border-box}
html,body{width:1200px;height:901px;overflow:hidden}
body{background:radial-gradient(ellipse at 50% 45%,#f7f7f8 0%,var(--bg) 70%,#dcdedf 100%);font-family:"Roboto",Arial,sans-serif;position:relative}
.piece{position:absolute}
.blue{background:radial-gradient(ellipse at 50% 45%,var(--blue-light) 0%,var(--blue) 45%,var(--blue-deep) 100%)}
.wordmark{font-family:"Exo 2",Arial,sans-serif;font-weight:800;color:var(--white);letter-spacing:1px;line-height:1}
.wordmark.dark{color:var(--ink)}
.tiny{font-size:7px;color:var(--white);letter-spacing:.5px;position:absolute;white-space:nowrap}
.center{display:flex;align-items:center;justify-content:center}

/* gift box dieline */
.box-flap-top{left:134px;top:36px;width:231px;height:61px}
.box-flap-top .wordmark{font-size:24px;transform:rotate(180deg)}
.box-main{left:68px;top:100px;width:365px;height:362px}
.box-main .wordmark{font-size:40px}
.box-main .side-text{left:26px;top:150px;transform:rotate(90deg);transform-origin:left top}
.box-flap-bottom{left:134px;top:466px;width:231px;height:56px;padding:8px 14px;display:flex;gap:4px}
.spec-cell{flex:1;background:#d7eefb;font-size:7px;color:var(--ink);text-align:center;padding-top:2px;border-top:9px solid var(--blue-deep)}

/* polybag */
.polybag{left:442px;top:34px;width:268px;height:416px}
.polybag .handle{position:absolute;left:94px;top:28px;width:80px;height:28px;border-radius:14px;background:var(--bg)}
.polybag .wordmark{font-size:34px}

/* watch pads */
.pad{width:58px;height:58px}
.pad.round{border-radius:50%}
.pad.square{border-radius:10px}
.pad.rim{background:linear-gradient(145deg,#eef0f2,var(--silver-dark));padding:8px}
.pad .face{width:100%;height:100%;border-radius:inherit}
.pad .wordmark{font-size:11px}

/* shopping bag */
.shopper{left:741px;top:200px;width:389px;height:250px}
.shopper .wordmark{font-size:30px;position:absolute;right:40px;top:62px}
.shopper .side-mark{left:30px;top:120px;font-size:20px}
.rope{left:1010px;top:150px}

/* strap sleeves */
.sleeve{top:540px;width:49px;height:322px;background:var(--white);box-shadow:0 0 0 1px var(--line)}
.sleeve .cap{position:absolute;left:0;right:0;top:12px;height:3px;background:#d2403a}
.sleeve .wordmark{position:absolute;left:50%;top:50%;transform:translate(-50%,-50%) rotate(90deg);font-size:34px}
.sleeve.small .wordmark{font-size:14px;transform:translate(-50%,-50%)}

/* hang tags */
.tag{width:128px;height:38px;border-radius:4px 12px 12px 4px}
.tag .wordmark{font-size:15px}
.tag-diamond{width:56px;height:56px;transform:rotate(45deg);border-radius:6px}
.tag-diamond .wordmark{transform:rotate(-45deg);font-size:14px}

/* cross box */
.cross .wordmark{font-size:24px}

/* warranty folders */
.folder{left:705px;width:425px;display:flex;box-shadow:0 1px 3px rgba(0,0,0,.15)}
.folder .panel{flex:1;position:relative}
.folder .white{background:var(--white)}
.folder .wordmark{font-size:22px}
.warranty-label{position:absolute;top:14px;left:50%;transform:translateX(-50%);background:var(--white);color:var(--blue-deep);font-size:8px;font-weight:700;padding:2px 5px;white-space:nowrap}
.form-field{height:16px;background:var(--white);margin:0 10px 8px;font-size:7px;color:var(--ink);padding:3px 4px}
.silver-band{position:absolute;left:0;right:0;bottom:30px;height:10px;background:linear-gradient(var(--white),var(--silver))}
</style>
</head>
<body>

<!-- Gift box dieline -->
<div class="piece box-flap-top blue center"><span class="wordmark">Kemra</span></div>
<div class="piece box-main blue center">
  <span class="wordmark">ZOLT</span>
  <span class="tiny side-text">digital time for everyone</span>
  <span class="tiny" style="bottom:12px;left:50%;transform:translateX(-50%)">www.zoltwatches.com</span>
</div>
<div class="piece box-flap-bottom blue">
  <div class="spec-cell">Model</div><div class="spec-cell">Colour</div><div class="spec-cell">Size</div><div class="spec-cell">Batch</div><div class="spec-cell">Date</div>
</div>

<!-- Polybag -->
<div class="piece polybag blue center">
  <div class="handle"></div>
  <span class="wordmark">ZOLT</span>
  <span class="tiny" style="bottom:14px;left:50%;transform:translateX(-50%)">www.zoltwatches.com</span>
</div>

<!-- Watch pads -->
<div class="piece pad round blue center" style="left:768px;top:34px"><span class="wordmark">ZOLT</span></div>
<div class="piece pad round blue center" style="left:858px;top:34px"><span class="wordmark">ZOLT</span></div>
<div class="piece pad square blue center" style="left:948px;top:34px"><span class="wordmark">ZOLT</span></div>
<div class="piece pad square blue center" style="left:1038px;top:34px"><span class="wordmark">ZOLT</span></div>
<div class="piece pad round rim" style="left:768px;top:100px"><div class="face blue center"><span class="wordmark">ZOLT</span></div></div>
<div class="piece pad round rim" style="left:858px;top:100px"><div class="face blue center"><span class="wordmark">ZOLT</span></div></div>
<div class="piece pad square rim" style="left:948px;top:100px"><div class="face blue center"><span class="wordmark">ZOLT</span></div></div>
<div class="piece pad square rim" style="left:1038px;top:100px"><div class="face blue center"><span class="wordmark">ZOLT</span></div></div>

<!-- Shopping bag -->
<svg class="piece rope" width="90" height="60" viewBox="0 0 90 60"><path d="M12 60 C10 20 20 4 40 4 C62 4 74 22 72 60" fill="none" stroke="#1b1b1b" stroke-width="3"/></svg>
<div class="piece shopper blue">
  <span class="wordmark">ZOLT</span>
  <span class="wordmark piece side-mark">ZOLT</span>
  <span class="tiny" style="bottom:12px;left:30px">www.zoltwatches.com</span>
</div>

<!-- Strap sleeves -->
<div class="piece sleeve" style="left:68px"><div class="cap"></div><span class="wordmark dark">ZOLT</span></div>
<div class="piece sleeve blue" style="left:146px"><div class="cap" style="background:var(--white)"></div><span class="wordmark">ZOLT</span></div>
<div class="piece sleeve small" style="left:219px"><div class="cap"></div><span class="wordmark dark">ZOLT</span></div>
<div class="piece sleeve" style="left:292px;width:53px"><div class="cap"></div><span class="wordmark dark">ZOLT</span></div>

<!-- Hang tags -->
<svg class="piece" style="left:370px;top:470px" width="330" height="130" viewBox="0 0 330 130">
  <path d="M0 20 Q10 8 22 26 M0 74 Q12 60 26 78" fill="none" stroke="#555" stroke-width="1.2"/>
  <path d="M196 0 L200 30 M266 0 L272 30" fill="none" stroke="#555" stroke-width="1.2"/>
</svg>
<div class="piece tag blue center" style="left:392px;top:482px"><span class="wordmark">ZOLT</span></div>
<div class="piece tag blue center" style="left:396px;top:532px"><span class="wordmark">ZOLT</span></div>
<div class="piece tag-diamond blue center" style="left:542px;top:510px"><span class="wordmark">ZOLT</span></div>
<div class="piece tag-diamond blue center" style="left:614px;top:510px"><span class="wordmark">ZOLT</span></div>

<!-- Cross box dieline -->
<div class="piece cross blue center" style="left:462px;top:620px;width:134px;height:65px"><span class="wordmark" style="transform:rotate(180deg)">Kemra</span></div>
<div class="piece cross blue" style="left:370px;top:685px;width:92px;height:117px"></div>
<div class="piece cross blue center" style="left:462px;top:685px;width:134px;height:117px;box-shadow:inset 0 0 0 1px rgba(255,255,255,.35)"></div>
<div class="piece cross blue" style="left:596px;top:685px;width:89px;height:117px"></div>
<div class="piece cross blue center" style="left:462px;top:802px;width:134px;height:60px"><span class="wordmark">ZOLT</span></div>
<div class="piece blue" style="left:600px;top:612px;width:56px;height:56px;transform:rotate(45deg) scaleY(.6);border-radius:3px"></div>

<!-- Warranty folder, outside -->
<div class="piece folder" style="top:523px;height:169px">
  <div class="panel blue"></div>
  <div class="panel blue"><div class="silver-band"></div></div>
  <div class="panel white center" style="align-items:flex-end;padding-bottom:10px"><span class="wordmark dark">ZOLT</span></div>
  <div class="panel blue center">
    <span class="warranty-label">WARRANTY CARD</span>
    <span class="wordmark">ZOLT</span>
  </div>
</div>

<!-- Warranty folder, inside -->
<div class="piece folder" style="top:705px;height:157px">
  <div class="panel blue" style="padding-top:14px">
    <p class="tiny" style="position:static;margin:0 10px 8px">Keep this card safe</p>
    <div class="form-field">Name</div><div class="form-field">Model</div><div class="form-field">Date</div>
  </div>
  <div class="panel blue"></div>
  <div class="panel white center" style="align-items:flex-end;padding-bottom:10px"><span class="wordmark dark">ZOLT</span></div>
  <div class="panel blue center" style="align-items:flex-end;padding-bottom:14px"><span class="wordmark">ZOLT</span></div>
</div>

</body>
</html>
```